Three Self-help Book Covers for BRG

We need three book covers designed.

We have a good idea what the three designs will be and our directions are attached along with sample artwork.

1-Nine Quiet Lanterns
2-The PaperKite Almanac
3-The Driftwood

My schools website is: www.BrightmoorRiverGuild.example

Target Market(s)

Self-help

Industry/Entity Type

Life Coaching

Font styles to use
Other font styles liked:
• See Attachment for details

Requirements
Must have
• See Attached Suggestions
Nice to have
Should not have

```html
<!DOCTYPE html>
<html lang="en">
<head>
<meta charset="utf-8">
<title>BRG – Three Book Covers</title>
<link rel="stylesheet" href="https://fonts.googleapis.com/css2?family=Josefin+Sans:wght@400;600&family=Cinzel:wght@400;700&family=Playfair+Display:wght@400;700&family=Exo+2:wght@600;800&family=Montserrat:wght@400;600;700&display=swap">
<style>
  :root {
    --backdrop: #e9eaec;
    --navy: #0f2a5c;
    --navy-deep: #0a1f4a;
    --sky-top: #4f9fe0;
    --sky-glow: #eaf6ff;
    --water: #1f6fc0;
    --ice-text: #13295a;
    --pale-blue: #9fd0ff;
    --crimson: #6d0a08;
    --ember: #e23b12;
    --night: #150303;
    --gold: #d8a84a;
    --ivory: #f5ecd9;
    --aqua-top: #4fb8e4;
    --aqua-glow: #e9f8ff;
    --title-ice: #e6f6ff;
    --title-edge: #4a8fc4;
    --ink: #1b2a3f;
    --badge: #c9b98a;
  }
  * { box-sizing: border-box; margin: 0; padding: 0; }
  html, body { width: 1200px; height: 856px; overflow: hidden; }
  body { background: var(--backdrop); position: relative; font-family: "Montserrat", sans-serif; }

  .cover { position: absolute; overflow: hidden; box-shadow: 0 10px 24px rgba(0,0,0,.25); }
  .brand { display: flex; flex-direction: column; align-items: center; gap: 3px; }
  .brand-dot { width: 24px; height: 24px; border-radius: 50%; background: var(--badge); }
  .brand-name { font-size: 9px; font-weight: 600; letter-spacing: 1px; }

  /* Cover 1 */
  .almanac { left: 176px; top: 311px; width: 266px; height: 411px;
    background: linear-gradient(180deg, var(--sky-top) 0%, var(--sky-glow) 38%, var(--water) 41%, var(--navy-deep) 72%); }
  .almanac .brand { position: absolute; top: 14px; left: 0; right: 0; }
  .almanac .brand-name { color: var(--navy); }
  .almanac-title { position: absolute; top: 68px; width: 100%; text-align: center;
    font-family: "Josefin Sans", sans-serif; font-weight: 400; font-size: 19px; color: var(--navy-deep); }
  .almanac-sub { position: absolute; top: 94px; width: 100%; text-align: center;
    font-family: "Josefin Sans", sans-serif; font-size: 8px; color: var(--navy-deep); }
  .almanac-art { position: absolute; left: 48px; top: 110px; width: 170px; height: 210px;
    background: radial-gradient(closest-side, rgba(235,247,255,.95), rgba(150,205,240,.55) 60%, rgba(150,205,240,0) 100%); }
  .virtues { position: absolute; top: 168px; width: 100%; text-align: center;
    font-family: "Playfair Display", serif; color: var(--ice-text); line-height: 1.05; }
  .virtues span { display: block; }
  .v1 { font-size: 22px; } .v2 { font-size: 13px; } .v3 { font-size: 22px; } .v4 { font-size: 15px; } .v5 { font-size: 14px; }
  .almanac-foot { position: absolute; bottom: 0; width: 100%; height: 120px; background: var(--navy-deep);
    color: #fff; text-align: center; padding-top: 22px; font-size: 9.5px; line-height: 1.35; }
  .almanac-foot small { font-size: 6px; }
  .almanac-author { margin-top: 18px; color: var(--pale-blue); font-size: 10px; }

  /* Cover 2 */
  .lanterns { left: 448px; top: 258px; width: 312px; height: 481px;
    background: radial-gradient(ellipse at 50% 38%, var(--ember) 0%, var(--crimson) 35%, var(--night) 72%); }
  .lanterns-title { position: absolute; top: 22px; width: 100%; text-align: center;
    font-family: "Cinzel", serif; color: var(--gold); font-size: 24px; line-height: 1.15; letter-spacing: 1px; font-weight: 400; }
  .rule { display: block; width: 200px; height: 1px; background: var(--gold); margin: 2px auto 0; }
  .lanterns-art { position: absolute; left: 20px; top: 80px; width: 272px; height: 260px;
    background: radial-gradient(closest-side at 50% 40%, #ffd24a 0%, #f07a16 35%, rgba(160,20,8,.35) 75%, rgba(0,0,0,0) 100%); }
  .gift { position: absolute; top: 222px; font-family: "Playfair Display", serif; font-size: 9px;
    color: var(--night); font-weight: 700; letter-spacing: .5px; transform-origin: left center; white-space: nowrap; }
  .lanterns-tag { position: absolute; top: 348px; width: 100%; text-align: center;
    font-family: "Playfair Display", serif; color: var(--ivory); font-size: 18px; line-height: 1.25; }
  .lanterns-tag u { text-underline-offset: 3px; }
  .lanterns-author { position: absolute; top: 418px; width: 100%; text-align: center;
    font-family: "Playfair Display", serif; color: var(--gold); font-size: 12px; }

  /* Cover 3 */
  .driftwood { left: 766px; top: 334px; width: 259px; height: 387px;
    background: radial-gradient(ellipse at 50% 10%, var(--aqua-glow) 0%, var(--aqua-top) 75%); }
  .driftwood .brand { position: absolute; top: 14px; left: 0; right: 0; }
  .driftwood .brand-name { color: var(--ink); }
  .driftwood-heading { position: absolute; top: 62px; width: 100%; text-align: center; color: var(--ink); }
  .dw-the { font-family: "Exo 2", sans-serif; font-weight: 600; font-size: 12px; letter-spacing: 1px; }
  .dw-main { font-family: "Exo 2", sans-serif; font-weight: 800; font-size: 25px; color: var(--title-ice);
    letter-spacing: 1px; line-height: 1.05; -webkit-text-stroke: .6px var(--title-edge); }
  .dw-of { font-family: "Montserrat", sans-serif; font-size: 8px; font-weight: 600; margin-top: 2px; }
  .dw-trans { font-family: "Montserrat", sans-serif; font-size: 15px; font-weight: 700; line-height: 1.1; }
  .dw-powers { font-family: "Montserrat", sans-serif; font-size: 9px; font-weight: 600; letter-spacing: .5px; }
  .driftwood-art { position: absolute; left: 12px; top: 140px; width: 236px; height: 220px;
    background: radial-gradient(closest-side, rgba(210,235,255,.9), rgba(120,160,210,.45) 60%, rgba(79,184,228,0) 100%); }
  .driftwood-author { position: absolute; bottom: 12px; width: 100%; text-align: center; font-size: 7px; color: var(--ink); }
</style>
</head>
<body>

<section class="cover almanac">
  <div class="brand"><span class="brand-dot"></span><span class="brand-name">BRG</span></div>
  <h2 class="almanac-title">The PaperKite Almanac</h2>
  <p class="almanac-sub">A Guide Book for the Inner You</p>
  <div class="almanac-art" role="img" aria-label="Iceberg floating in a bright sky and sunlit sea"></div>
  <p class="virtues"><span class="v1">HOPE</span><span class="v2">FAITH</span><span class="v3">PEACE</span><span class="v4">LOVE</span><span class="v5">BELIEVE</span></p>
  <div class="almanac-foot">
    Drawn from the Life Coaching<br>Practice that’s Guiding people forward<br>“one step at a time” <small>The LioMethod™</small>
    <p class="almanac-author">By Master Coach Lio Varenne</p>
  </div>
</section>

<section class="cover lanterns">
  <h2 class="lanterns-title">Nine Quiet<br>Lanterns<span class="rule"></span></h2>
  <div class="lanterns-art" role="img" aria-label="Glowing bird with rays of light streaming downward"></div>
  <span class="gift" style="left:88px; transform: rotate(64deg);">WISDOM</span>
  <span class="gift" style="left:112px; transform: rotate(72deg);">UNDERSTANDING</span>
  <span class="gift" style="left:134px; transform: rotate(80deg);">COUNSEL</span>
  <span class="gift" style="left:152px; transform: rotate(86deg);">FORTITUDE</span>
  <span class="gift" style="left:170px; transform: rotate(94deg); top:212px;">KNOWLEDGE</span>
  <span class="gift" style="left:192px; transform: rotate(104deg); top:207px;">PITY</span>
  <span class="gift" style="left:214px; transform: rotate(114deg); top:202px;">FEAR OF GOD</span>
  <p class="lanterns-tag">TO GUIDE YOU BACK<br><u>TO YOUR… INNER SELF</u></p>
  <p class="lanterns-author">Master Coach Lio Varenne</p>
</section>

<section class="cover driftwood">
  <div class="brand"><span class="brand-dot"></span><span class="brand-name">BRG</span></div>
  <div class="driftwood-heading">
    <p class="dw-the">THE</p>
    <h2 class="dw-main">DRIFTWOOD</h2>
    <p class="dw-of">Toward Your</p>
    <p class="dw-trans">Restorative</p>
    <p class="dw-powers">Tides of Calm and Kindness</p>
  </div>
  <div class="driftwood-art" role="img" aria-label="Blue heart-shaped tree with butterflies taking flight"></div>
  <p class="driftwood-author">Master Coach Lio Varenne</p>
</section>

</body>
</html>
```